Kevmoor belly band - cardboard to wrap around a plain tin for Gift

We are packaging men's and ladies handkerchiefs into tins for Gifts. We need two belly band designs to wrap around a small tin which measures 140 x 100 x 43 depth. The band to measure approx 90 w x 330 long inclusive is 30mm lapover . The ladies design (white tin) to have a subtle floral background with the word .Kevmoor. only placed on front centre of tin. The men's (black tin) to have a masculine look with the logo .Kevmoor. (the word can be taken out of the oval logo. This to placed in centre on front of tin. Men's could have a tan or cream textured look??

Target Market(s)

30 to 80 year old market

Font styles to use
Other font styles liked:
• Mona lisa

Colors

Designer to choose colors to be used in the design.

Requirements
Must have
• Two different designs one for men's black tin and one for ladies white tin.
• Must have continuous design with logo in centre once wrapped around the tin.
• Both must have an upmarket classy look.
• Tins will be displayed horizontal.
Nice to have
• Ladies would like to see soft floral not too over the top feminine classy look.
• Mens more masculine and upmarket maybe plain with a textured look.
• A design has been attached - like this sort of look for ladies!

```html
<!DOCTYPE html>
<html lang="en">
<head>
<meta charset="utf-8">
<title>Kevmoor Belly Bands</title>
<link rel="stylesheet" href="https://fonts.googleapis.com/css2?family=Arimo:wght@700&family=Bodoni+Moda:wght@500&display=swap">
<style>
  :root {
    --canvas: #ffffff;
    --tan: #c9923f;
    --tan-light: #d6a452;
    --tan-dark: #b88135;
    --band-white: #ffffff;
    --ink: #161412;
    --stitch-dark: #3a2a1a;
    --stitch-pink: #e4cfd3;
    --leaf-sage: #a9c4bd;
    --leaf-green: #8fae9c;
    --leaf-rose: #d9b3aa;
    --leaf-grey: #c3c7c2;
  }
  html, body {
    margin: 0;
    padding: 0;
    width: 1200px;
    height: 1091px;
    overflow: hidden;
    background: var(--canvas);
  }
  .sheet {
    position: relative;
    width: 1200px;
    height: 1091px;
    background: var(--canvas);
  }
  .band {
    position: absolute;
    top: 37px;
    height: 1002px;
  }
  .band--leather {
    background: linear-gradient(160deg, var(--tan-light) 0%, var(--tan) 45%, var(--tan-dark) 100%);
  }
  .band--floral { background: var(--band-white); }
  .band--men-front { left: 40px; width: 275px; }
  .band--women-front { left: 323px; width: 273px; }
  .band--women-side { left: 604px; width: 273px; }
  .band--men-side { left: 885px; width: 274px; }

  .foliage {
    position: absolute;
    top: 0;
    height: 100%;
    width: 83px;
    background:
      linear-gradient(180deg,
        var(--leaf-sage) 0%, var(--leaf-rose) 12%, var(--leaf-green) 24%,
        var(--leaf-grey) 36%, var(--leaf-sage) 48%, var(--leaf-rose) 60%,
        var(--leaf-green) 72%, var(--leaf-grey) 84%, var(--leaf-sage) 100%);
    opacity: 0.55;
  }
  .foliage--left {
    left: 0;
    -webkit-mask-image: linear-gradient(90deg, #000 40%, transparent 100%);
    mask-image: linear-gradient(90deg, #000 40%, transparent 100%);
  }
  .foliage--right {
    right: 0;
    -webkit-mask-image: linear-gradient(270deg, #000 40%, transparent 100%);
    mask-image: linear-gradient(270deg, #000 40%, transparent 100%);
  }

  .stitching {
    position: absolute;
    left: 0;
    top: 0;
    width: 1200px;
    height: 1091px;
  }

  .brand-block {
    position: absolute;
    width: 280px;
    text-align: center;
    color: var(--ink);
    transform: translate(-50%, -50%);
  }
  .brand-block--turned {
    transform: translate(-50%, -50%) rotate(-90deg);
  }
  .brand-name {
    font-family: "Arimo", Arial, sans-serif;
    font-weight: 700;
    font-size: 46px;
    line-height: 48px;
    letter-spacing: 1px;
    margin: 0;
  }
  .brand-tagline {
    font-family: "Arimo", Arial, sans-serif;
    font-weight: 700;
    font-size: 12.2px;
    line-height: 14px;
    letter-spacing: 0.1px;
    margin: 10px 0 0;
  }
  .brand-since {
    font-family: "Bodoni Moda", "Didot", serif;
    font-weight: 500;
    font-size: 14px;
    line-height: 17px;
    margin: 26px 0 0;
  }
  .brand-block--turned .brand-tagline { margin-top: 25px; }
  .brand-block--turned .brand-since { margin-top: 40px; }
</style>
</head>
<body>
<main class="sheet">
  <section class="band band--leather band--men-front" role="img" aria-label="Tan textured leather-look surface"></section>
  <section class="band band--floral band--women-front">
    <div class="foliage foliage--left" role="img" aria-label="Soft watercolour eucalyptus and leaf border"></div>
    <div class="foliage foliage--right" role="img" aria-label="Soft watercolour eucalyptus and leaf border"></div>
  </section>
  <section class="band band--floral band--women-side">
    <div class="foliage foliage--left" role="img" aria-label="Soft watercolour eucalyptus and leaf border"></div>
    <div class="foliage foliage--right" role="img" aria-label="Soft watercolour eucalyptus and leaf border"></div>
  </section>
  <section class="band band--leather band--men-side" role="img" aria-label="Tan textured leather-look surface"></section>

  <svg class="stitching" viewBox="0 0 1200 1091" aria-hidden="true">
    <g stroke="var(--stitch-dark)" stroke-width="2" stroke-dasharray="13 9">
      <line x1="178" y1="37" x2="178" y2="402"/>
      <line x1="178" y1="666" x2="178" y2="1039"/>
      <line x1="1025" y1="37" x2="1025" y2="418"/>
      <line x1="1025" y1="660" x2="1025" y2="1039"/>
    </g>
    <g stroke="var(--stitch-pink)" stroke-width="2" stroke-dasharray="13 9">
      <line x1="460" y1="37" x2="460" y2="402"/>
      <line x1="460" y1="666" x2="460" y2="1039"/>
      <line x1="742" y1="37" x2="742" y2="418"/>
      <line x1="742" y1="660" x2="742" y2="1039"/>
    </g>
  </svg>

  <div class="brand-block" style="left:178px; top:532px;">
    <p class="brand-name">Kevmoor</p>
    <p class="brand-tagline">DESIGNER HANDKERCHIEFS</p>
    <p class="brand-since">Since 1958</p>
  </div>
  <div class="brand-block" style="left:460px; top:532px;">
    <p class="brand-name">Kevmoor</p>
    <p class="brand-tagline">DESIGNER HANDKERCHIEFS</p>
    <p class="brand-since">Since 1958</p>
  </div>
  <div class="brand-block brand-block--turned" style="left:739px; top:542px;">
    <p class="brand-name">Kevmoor</p>
    <p class="brand-tagline">DESIGNER HANDKERCHIEFS</p>
    <p class="brand-since">Since 1958</p>
  </div>
  <div class="brand-block brand-block--turned" style="left:1021px; top:542px;">
    <p class="brand-name">Kevmoor</p>
    <p class="brand-tagline">DESIGNER HANDKERCHIEFS</p>
    <p class="brand-since">Since 1958</p>
  </div>
</main>
</body>
</html>
```